Used Car Business Card Design

Maple Ridge Auto Sales is a woman owned women friendly car lot.  We focus on providing Professionalism, Integrity and Respect beginning with the initial introduction.  We place the highest importance on customer service after the sale and our rating with the TVB of Arkansas shows it.  We're starting out 7th year, recently relocated. Satisfied Clients bring their family members, friends and co-workers to buy their cars, SUV's and trucks from MRAS.
You buy here / you pay here, Lending program opportunities too, Great Cash Prices
Finance with Flexibility we look at each individual uniquely and not a credit score
I think of my kids when getting our vehicles ready and your safety when you drive away in a MRAS car. . .  Drive away with Peace of Mind...
Maroon, Black and Silver colors.

Updates
I sent a response to the designers - have  not heard from them, will I receive my funds back?

Thank you all,  a lot of great designs - Making my decision on Nov 4th

So much talent. . .
So very challenging. . .
Thank you for your participation.
Sincerely,
Maple Ridge Auto Sales
Lorna Pickett

Industry/Entity Type
Safety
Contact Information for Business Card
Maple Ridge Auto Sales
"A Sound Car at a Fair Price"
4153 Garvey Rd. Pine Hollow, Ar 72190
Lorna Pickett
501.389.7312

```html
<!DOCTYPE html>
<html lang="en">
<head>
<meta charset="utf-8">
<title>Maple Ridge Auto Sales – Business Card</title>
<link rel="stylesheet" href="https://fonts.googleapis.com/css2?family=Michroma&family=Arimo:wght@400&display=swap">
<style>
  :root {
    --backdrop: #d6d6d8;
    --card-black: #0d0d0e;
    --card-sheen: #3a3a3d;
    --maroon: #c4161c;
    --maroon-deep: #8e0e12;
    --maroon-light: #e8383d;
    --silver: #e9e9ea;
    --divider: #8a8a8d;
  }
  * { box-sizing: border-box; margin: 0; padding: 0; }
  html, body {
    width: 1200px;
    height: 855px;
    overflow: hidden;
    background: var(--backdrop);
  }
  .stage {
    position: relative;
    width: 1200px;
    height: 855px;
  }
  .card {
    position: absolute;
    top: 279px;
    width: 520px;
    height: 297px;
    border-radius: 18px;
    overflow: hidden;
    background:
      linear-gradient(118deg, var(--card-black) 0%, var(--card-black) 38%, var(--card-sheen) 52%, var(--card-black) 68%, var(--card-black) 100%);
    box-shadow: 0 6px 18px rgba(0,0,0,0.25);
  }
  .card--front { left: 60px; }
  .card--back  { left: 620px; }

  .band {
    position: absolute;
    left: 0;
    right: 0;
    bottom: 0;
    height: 56px;
    border-top: 3px solid var(--silver);
    background: linear-gradient(180deg, var(--maroon-light) 0%, var(--maroon) 45%, var(--maroon-deep) 100%);
    display: flex;
    align-items: center;
    justify-content: center;
    font-family: "Arimo", sans-serif;
    font-size: 17px;
    color: var(--silver);
    letter-spacing: 0.5px;
    white-space: nowrap;
  }
  .band__gap { display: inline-block; width: 22px; }

  /* Front */
  .brand {
    position: absolute;
    top: 86px;
    left: 0;
    right: 0;
    text-align: center;
    font-family: "Michroma", sans-serif;
    color: var(--silver);
    line-height: 1.25;
    white-space: nowrap;
  }
  .brand__name {
    font-size: 28px;
    letter-spacing: 5px;
  }
  .brand__sub {
    font-size: 15px;
    letter-spacing: 3px;
    padding-left: 170px;
  }

  /* Back */
  .vehicle-mark {
    position: absolute;
    left: 34px;
    top: 42px;
    width: 150px;
    height: 150px;
    border-radius: 12px;
    background: linear-gradient(160deg, var(--maroon-light), var(--maroon-deep));
    opacity: 0.9;
  }
  .divider {
    position: absolute;
    left: 208px;
    top: 40px;
    width: 1px;
    height: 160px;
    background: var(--divider);
  }
  .contact {
    position: absolute;
    left: 226px;
    right: 14px;
    top: 62px;
    color: var(--silver);
    font-family: "Arimo", sans-serif;
    white-space: nowrap;
  }
  .contact__name {
    font-family: "Michroma", sans-serif;
    font-size: 19px;
    letter-spacing: 1.5px;
    margin-bottom: 18px;
  }
  .contact__line {
    font-size: 17px;
    line-height: 1.45;
    display: flex;
    align-items: center;
    gap: 8px;
  }
  .contact__icon { width: 16px; height: 16px; flex: none; }
</style>
</head>
<body>
  <main class="stage">
    <section class="card card--front" aria-label="Business card front">
      <div class="brand">
        <div class="brand__name">MAPLE RIDGE</div>
        <div class="brand__sub">AUTO SALES</div>
      </div>
      <div class="band">A Sound Car at a Fair Price</div>
    </section>

    <section class="card card--back" aria-label="Business card back">
      <div class="vehicle-mark" role="img" aria-label="Red front-view car illustration"></div>
      <div class="divider"></div>
      <div class="contact">
        <div class="contact__name">LORNA PICKETT</div>
        <div class="contact__line">
          <svg class="contact__icon" viewBox="0 0 16 16" aria-hidden="true">
            <circle cx="8" cy="8" r="8" fill="var(--maroon)"/>
            <rect x="5.2" y="3.2" width="5.6" height="9.6" rx="1.2" fill="none" stroke="#fff" stroke-width="1.2"/>
            <circle cx="8" cy="11" r="0.7" fill="#fff"/>
          </svg>
          <span>501.389.7312</span>
        </div>
        <div class="contact__line">4153 Garvey Rd.</div>
        <div class="contact__line">Pine Hollow, Ar 72190</div>
      </div>
      <div class="band">You buy here<span class="band__gap"></span>You pay here</div>
    </section>
  </main>
</body>
</html>
```